PowerPoint template for a tech startup

We need a PowerPoint template with a title slide, text slide, section slide, and thank you slide.
Our application helps engineering teams to be more productive. We would love a design that is slick, sophisticated, and consistent with our brand. (see more at www.tandrel.example or attached files)
By the way (not a requirement), Tandrel means lighthouse in Greek.
Also, here is the font we used (not required) - https://typeshelf.example/fonts/sample-face

• https://typeshelf.example/fonts/sample-face

```html
<!DOCTYPE html>
<html lang="en">
<head>
<meta charset="utf-8">
<title>Tandrel — Presentation Template</title>
<link href="https://fonts.googleapis.com/css2?family=League+Gothic&family=Open+Sans:wght@400;600&display=swap" rel="stylesheet">
<style>
  :root {
    --backdrop: #b8cad6;
    --navy: #124e72;
    --orange: #e8560f;
    --white: #ffffff;
    --ink: #1d1d1d;
    --photo-city-a: #2b3440;
    --photo-city-b: #c9d3dc;
    --photo-desk-a: #e9e9e7;
    --photo-desk-b: #3a3a3a;
  }
  * { box-sizing: border-box; margin: 0; padding: 0; }
  html, body { width: 1200px; height: 734px; overflow: hidden; background: var(--backdrop); }
  .canvas { position: relative; width: 1200px; height: 734px; }

  .slide { position: absolute; width: 527px; height: 297px; background: var(--white); overflow: hidden; }
  .slide--title   { left: 62px;  top: 46px; }
  .slide--section { left: 618px; top: 46px; }
  .slide--text    { left: 62px;  top: 382px; }
  .slide--closing { left: 618px; top: 382px; background: var(--navy); }

  .display { font-family: "League Gothic", "Oswald", sans-serif; font-weight: 400; line-height: 1; }
  .body { font-family: "Open Sans", Arial, sans-serif; font-size: 6.6px; line-height: 10.5px; color: var(--ink); }

  .accent-bar { position: absolute; left: 0; top: 0; width: 100%; height: 8px; background: var(--orange); }

  /* Title slide */
  .brand { position: absolute; left: 24px; top: 34px; color: var(--navy); font-size: 56px; letter-spacing: 1px; }
  .slide--title .heading { position: absolute; left: 24px; top: 154px; font-size: 36px; color: var(--navy); }
  .slide--title .lead { position: absolute; left: 24px; top: 188px; width: 200px; }
  .legal { position: absolute; left: 24px; top: 280px; font-family: "Open Sans", Arial, sans-serif; font-size: 4px; color: var(--navy); }
  .title-panel { position: absolute; left: 263px; top: 0; width: 264px; height: 100%; background: var(--navy); }

  /* Section slide */
  .section-panel { position: absolute; left: 0; top: 8px; width: 163px; height: 289px; background: var(--navy); }
  .section-panel .heading { position: absolute; left: 25px; top: 62px; font-size: 24px; color: var(--orange); }
  .section-panel .body { position: absolute; left: 25px; top: 93px; width: 112px; color: var(--white); }
  .feature { position: absolute; top: 60px; width: 96px; text-align: center; }
  .feature--1 { left: 182px; } .feature--2 { left: 298px; } .feature--3 { left: 413px; }
  .feature__icon { display: block; margin: 0 auto; width: 52px; height: 52px; }
  .feature__title { margin-top: 6px; font-size: 14px; color: var(--orange); }
  .feature__subtitle { margin-top: 4px; font-size: 10px; color: var(--ink); }
  .feature .body { margin: 6px auto 0; width: 84px; }

  /* Text slide */
  .slide--text .heading { position: absolute; left: 24px; top: 28px; font-size: 24px; color: var(--orange); }
  .slide--text .intro { position: absolute; left: 24px; top: 64px; width: 480px; }
  .media { position: absolute; top: 117px; width: 219px; }
  .media--left { left: 24px; } .media--right { left: 287px; }
  .media__photo { width: 219px; height: 96px; }
  .media__photo--city { background: linear-gradient(160deg, var(--photo-city-b) 0%, var(--photo-city-a) 60%); }
  .media__photo--desk { background: linear-gradient(120deg, var(--photo-desk-b) 0%, var(--photo-desk-a) 35%, var(--photo-desk-a) 100%); }
  .media .body { margin-top: 13px; }

  /* Closing slide */
  .closing-title { position: absolute; left: 51px; top: 118px; font-size: 68px; color: var(--white); letter-spacing: 1px; }
</style>
</head>
<body>
<main class="canvas">

  <section class="slide slide--title">
    <div class="brand display">Tandrel</div>
    <h1 class="heading display">Title Slide</h1>
    <p class="lead body">Lorem ipsum dolor sit amet, consectetuer adipiscing Lorem ipsum dolor sit amet, consectetuer adipiscing elit, sed diam nonummy nibh</p>
    <p class="legal">© 2023, Tandrel, Inc.</p>
    <div class="title-panel"></div>
  </section>

  <section class="slide slide--section">
    <div class="accent-bar"></div>
    <div class="section-panel">
      <h2 class="heading display">Title Slide</h2>
      <p class="body">Lorem ipsum dolor sit amet, consectetuer adipiscing Lorem ipsum dolor sit amet, consectetuer adipiscing elit, sed diam nonummy nibh Lorem ipsum dolor sit amet, consectetuer adipiscing elit, sed diam nonummy nibh euismod tincidunt ut laoreet dolore magna aliquam erat volutpat. Ut wisi enim ad minim veniam, quis nostrud exerci tation ullamcorper suscipit lobortis nisl ut</p>
    </div>

    <div class="feature feature--1">
      <svg class="feature__icon" viewBox="0 0 52 52" aria-hidden="true">
        <circle cx="26" cy="26" r="26" fill="var(--orange)"/>
        <path d="M16 25 L26 16 L36 25 V36 H16 Z" fill="none" stroke="#fff" stroke-width="1.6" stroke-linejoin="round"/>
        <rect x="22" y="27" width="8" height="6" rx="1" fill="none" stroke="#fff" stroke-width="1.4"/>
      </svg>
      <h3 class="feature__title display">Headtitle</h3>
      <p class="feature__subtitle display">Subtitle</p>
      <p class="body">Lorem ipsum dolor sit amet, consectetuer adipiscing Lorem ipsum dolor sit amet, consectetuer adipiscing elit, sed diam nonummy nibh Lorem ipsum dolor sit amet, consectetuer adipiscing elit, sed diam nonummy nibh euismod tincidunt ut lao-</p>
    </div>

    <div class="feature feature--2">
      <svg class="feature__icon" viewBox="0 0 52 52" aria-hidden="true">
        <circle cx="26" cy="26" r="26" fill="var(--orange)"/>
        <rect x="18" y="14" width="16" height="24" rx="1.5" fill="none" stroke="#fff" stroke-width="1.6"/>
        <g fill="none" stroke="#fff" stroke-width="1.2">
          <rect x="21" y="18" width="3" height="3"/><rect x="28" y="18" width="3" height="3"/>
          <rect x="21" y="24" width="3" height="3"/><rect x="28" y="24" width="3" height="3"/>
          <path d="M24 38 V32 H28 V38"/>
        </g>
      </svg>
      <h3 class="feature__title display">Headtitle</h3>
      <p class="feature__subtitle display">Subtitle</p>
      <p class="body">Lorem ipsum dolor sit amet, consectetuer adipiscing Lorem ipsum dolor sit amet, consectetuer adipiscing elit, sed diam nonummy nibh Lorem ipsum dolor sit amet, consectetuer adipiscing elit, sed diam nonummy nibh euismod tincidunt ut lao-</p>
    </div>

    <div class="feature feature--3">
      <svg class="feature__icon" viewBox="0 0 52 52" aria-hidden="true">
        <circle cx="26" cy="26" r="26" fill="var(--orange)"/>
        <path d="M17 14 H35 V38 H19 A2 2 0 0 1 17 36 Z" fill="none" stroke="#fff" stroke-width="1.6" stroke-linejoin="round"/>
        <path d="M17 34 H35 M22 19 H31 M22 23 H31 M22 27 H31" stroke="#fff" stroke-width="1.2"/>
      </svg>
      <h3 class="feature__title display">Headtitle</h3>
      <p class="feature__subtitle display">Subtitle</p>
      <p class="body">Lorem ipsum dolor sit amet, consectetuer adipiscing Lorem ipsum dolor sit amet, consectetuer adipiscing elit, sed diam nonummy nibh Lorem ipsum dolor sit amet, consectetuer adipiscing elit, sed diam nonummy nibh euismod tincidunt ut lao-</p>
    </div>
  </section>

  <section class="slide slide--text">
    <div class="accent-bar"></div>
    <h2 class="heading display">Title Slide</h2>
    <p class="intro body">Lorem ipsum dolor sit amet, consectetuer adipiscing Lorem ipsum dolor sit amet, consectetuer adipiscing elit, sed diam nonummy nibh Lorem ipsum dolor sit amet, consectetuer adipiscing elit, sed diam nonummy nibh euismod tincidunt ut laoreet dolore magna aliquam erat volutpat. Ut wisi enim ad minim veniam, quis nostrud exerci tation ullamcorper suscipit lobortis nisl ut</p>
    <figure class="media media--left">
      <div class="media__photo media__photo--city" role="img" aria-label="Photo of glass office towers seen from below against a cloudy sky"></div>
      <figcaption class="body">Lorem ipsum dolor sit amet, consectetuer adipiscing Lorem ipsum dolor sit amet, consectetuer adipiscing elit, sed diam nonummy nibh Lorem ipsum dolor sit amet, consectetuer adipiscing elit, sed diam nonummy nibh euismod tincidunt ut laoreet dolore magna aliquam</figcaption>
    </figure>
    <figure class="media media--right">
      <div class="media__photo media__photo--desk" role="img" aria-label="Top-down photo of hands typing on a laptop at a white desk with a desk phone and coffee"></div>
      <figcaption class="body">Lorem ipsum dolor sit amet, consectetuer adipiscing Lorem ipsum dolor sit amet, consectetuer adipiscing elit, sed diam nonummy nibh Lorem ipsum dolor sit amet, consectetuer adipiscing elit, sed diam nonummy nibh euismod tincidunt ut laoreet dolore magna aliquam</figcaption>
    </figure>
  </section>

  <section class="slide slide--closing">
    <h2 class="closing-title display">THANK YOU</h2>
  </section>

</main>
</body>
</html>
```